New business card for civil engineering company - "Keystone Audit"

We need a business card designed for our new structural engineering company.

The company name is "Keystone Audit" logo files attached.

We would like the following:
* Two-sided card
* Simple design

Information to be placed on the card:
Name - Marcus Dellow
Job Title - Director / Structural Engineer
Credentials - BEng(Hons), CPEng, CMengNZ, IntPE(NZ)
Email - marcus.dellow@keystoneaudit.co.nz
mobile - 0219364058
website - www.keystoneaudit.co.nz

```html
<!DOCTYPE html>
<html lang="en">
<head>
<meta charset="utf-8">
<title>Keystone Audit — Business Card</title>
<link rel="stylesheet" href="https://fonts.googleapis.com/css2?family=Arimo:wght@400;700&family=Tinos&display=swap">
<style>
  :root {
    --backdrop: #e9e9e9;
    --card-white: #ffffff;
    --grey-light: #8c8c8c;
    --grey-dark: #6f6f6f;
    --grey-edge: #b5b5b5;
    --ink: #1e1e1e;
    --ink-soft: #3a3a3a;
    --on-grey: #ffffff;
  }
  * { margin: 0; padding: 0; box-sizing: border-box; }
  html, body { width: 1200px; height: 1200px; overflow: hidden; }
  body { background: var(--backdrop); position: relative; }

  .card {
    position: absolute;
    left: 240px;
    width: 720px;
    height: 408px;
    border-radius: 16px;
    overflow: hidden;
    background: var(--card-white);
    box-shadow: 0 6px 18px rgba(0,0,0,0.18);
  }
  .card-front { top: 150px; }
  .card-back  { top: 642px; }
  .card svg.card-art { position: absolute; inset: 0; width: 100%; height: 100%; display: block; }

  .brand-name {
    position: absolute;
    font-family: "Arimo", sans-serif;
    font-weight: 700;
    color: var(--ink-soft);
    letter-spacing: 1.5px;
    text-transform: uppercase;
    white-space: nowrap;
  }
  .card-front .brand-name { left: 72px; top: 268px; font-size: 18px; }
  .card-back .brand-name { left: 0; right: 0; text-align: center; top: 240px; font-size: 24px; }

  .identity {
    position: absolute;
    right: 40px;
    top: 70px;
    text-align: right;
    font-family: "Tinos", serif;
    color: var(--on-grey);
  }
  .identity .person-name { font-size: 24px; margin-bottom: 10px; }
  .identity .role, .identity .credentials { font-size: 15px; line-height: 22px; }

  .contact-list {
    position: absolute;
    right: 40px;
    top: 264px;
    list-style: none;
    font-family: "Arimo", sans-serif;
    font-size: 17px;
    color: var(--on-grey);
  }
  .contact-list li {
    display: flex;
    justify-content: flex-end;
    align-items: center;
    gap: 12px;
    height: 30px;
  }
  .contact-list svg { width: 15px; height: 15px; flex: none; }

  .partner-site {
    position: absolute;
    left: 0; right: 0;
    top: 302px;
    text-align: center;
    font-family: "Arimo", sans-serif;
    font-size: 17px;
    color: var(--ink);
  }
</style>
</head>
<body>

<section class="card card-front" aria-label="Card front">
  <svg class="card-art" viewBox="0 0 720 408" aria-hidden="true">
    <rect x="0" y="0" width="720" height="210" fill="var(--grey-light)"/>
    <rect x="0" y="210" width="720" height="198" fill="var(--grey-dark)"/>
    <path d="M0 0 H310 C352 120 340 290 232 408 H0 Z" fill="var(--grey-edge)"/>
    <path d="M0 0 H292 C334 120 322 290 214 408 H0 Z" fill="var(--card-white)"/>
  </svg>

  <div class="brand-name">Keystone Audit</div>

  <div class="identity">
    <div class="person-name">Marcus Dellow</div>
    <div class="role">Director / Structural Engineer</div>
    <div class="credentials">BEng(Hons), CPEng, CMengNZ, IntPE(NZ)</div>
  </div>

  <ul class="contact-list">
    <li>0219364058
      <svg viewBox="0 0 16 16" aria-hidden="true"><rect x="1" y="1" width="14" height="14" rx="3" fill="#fff"/><rect x="5" y="3" width="6" height="10" rx="1" fill="none" stroke="var(--grey-dark)" stroke-width="1.4"/></svg>
    </li>
    <li>marcus.dellow@keystoneaudit.co.nz
      <svg viewBox="0 0 16 16" aria-hidden="true"><rect x="1" y="1" width="14" height="14" rx="3" fill="#fff"/><rect x="3.5" y="5" width="9" height="6.5" fill="none" stroke="var(--grey-dark)" stroke-width="1.3"/><path d="M3.5 5 L8 8.8 L12.5 5" fill="none" stroke="var(--grey-dark)" stroke-width="1.3"/></svg>
    </li>
    <li>www.keystoneaudit.co.nz
      <svg viewBox="0 0 16 16" aria-hidden="true"><rect x="1" y="1" width="14" height="14" rx="3" fill="#fff"/><circle cx="8" cy="8" r="4.3" fill="none" stroke="var(--grey-dark)" stroke-width="1.3"/><path d="M3.7 8 H12.3 M8 3.7 C6 6 6 10 8 12.3 M8 3.7 C10 6 10 10 8 12.3" fill="none" stroke="var(--grey-dark)" stroke-width="1"/></svg>
    </li>
  </ul>
</section>

<section class="card card-back" aria-label="Card back">
  <svg class="card-art" viewBox="0 0 720 408">
    <defs>
      <linearGradient id="decor-left" x1="0" y1="0" x2="0" y2="1">
        <stop offset="0" stop-color="#7a7a7a"/>
        <stop offset="1" stop-color="#b3b3b3"/>
      </linearGradient>
      <linearGradient id="decor-right" x1="0" y1="0" x2="0" y2="1">
        <stop offset="0" stop-color="#c2c2c2"/>
        <stop offset="1" stop-color="#7d7d7d"/>
      </linearGradient>
    </defs>
    <rect role="img" aria-label="Grey geometric decoration area, left edge"
          x="0" y="0" width="110" height="408" fill="url(#decor-left)"/>
    <rect role="img" aria-label="Grey geometric decoration area, right edge"
          x="610" y="0" width="110" height="408" fill="url(#decor-right)"/>
  </svg>

  <div class="brand-name">Keystone Audit</div>
  <div class="partner-site">brightfieldhomes.co.nz</div>
</section>

</body>
</html>
```